Corvane Supplies Business Card

Professional business card that stand out to our potential customers. Front and back with clean modern design

Industry/Entity Type

Oil and gas

Contact Information for Business Card

Name, address, website , office phone and cell number

Requirements
Must have
• Editable files for each employee

```html
<!DOCTYPE html>
<html lang="en">
<head>
<meta charset="utf-8">
<title>Corvane Supplies Business Card</title>
<link href="https://fonts.googleapis.com/css2?family=Anton&family=Montserrat:wght@400;700;800&display=swap" rel="stylesheet">
<style>
  :root {
    --backdrop: #acacac;
    --card: #ffffff;
    --brand-red: #ee2024;
    --brand-cyan: #06b0d4;
    --ink: #111111;
    --muted: #555555;
  }
  * { margin: 0; padding: 0; box-sizing: border-box; }
  html, body { width: 1200px; height: 1000px; overflow: hidden; }
  body {
    background: var(--backdrop);
    font-family: "Montserrat", sans-serif;
    position: relative;
  }
  .card {
    position: absolute;
    background: var(--card);
    box-shadow: 6px 6px 8px rgba(60, 50, 40, 0.35);
    overflow: hidden;
  }
  /* Front */
  .card-front { left: 253px; top: 79px; width: 694px; height: 399px; }
  .front-name {
    position: absolute; left: 0; right: 0; top: 150px;
    text-align: center;
    font-weight: 800; font-size: 46px; letter-spacing: 1px;
    color: var(--brand-red);
    text-transform: uppercase;
  }
  .front-band {
    position: absolute; left: 0; bottom: 0; width: 100%; height: 78px;
    display: flex;
  }
  .front-band .band-red { width: 347px; background: var(--brand-red); }
  .front-band .band-gap { width: 4px; background: var(--card); }
  .front-band .band-cyan { flex: 1; background: var(--brand-cyan); }

  /* Back */
  .card-back { left: 251px; top: 530px; width: 694px; height: 399px; }
  .back-brand {
    position: absolute; left: 37px; top: 60px;
    display: flex; align-items: center; gap: 10px;
  }
  .back-brand .brand-square { width: 22px; height: 22px; background: var(--brand-red); }
  .back-brand .brand-name {
    font-weight: 800; font-size: 20px; color: var(--brand-red);
    text-transform: uppercase; letter-spacing: 0.5px;
  }
  .person-name {
    position: absolute; left: 37px; top: 214px;
    font-family: "Anton", sans-serif; font-size: 31px; line-height: 1.1;
    color: var(--ink);
  }
  .person-role {
    position: absolute; left: 37px; top: 253px;
    font-weight: 700; font-size: 15px; letter-spacing: 1.5px;
    color: var(--brand-cyan);
  }
  .divider {
    position: absolute; left: 37px; top: 282px; width: 623px; height: 2px;
    background: linear-gradient(to right, var(--brand-red) 0 180px, var(--brand-cyan) 180px 100%);
  }
  .contact-list {
    position: absolute; left: 37px; top: 300px; list-style: none;
  }
  .contact-list li {
    display: flex; align-items: center; gap: 9px;
    height: 24px; font-size: 17px; color: var(--muted);
  }
  .contact-list svg { width: 14px; height: 14px; flex: none; }
  .address {
    position: absolute; right: 35px; top: 326px;
    text-align: right; font-size: 17px; line-height: 24px; color: var(--muted);
  }
</style>
</head>
<body>
  <section class="card card-front">
    <div class="front-name">Corvane Supplies</div>
    <div class="front-band">
      <div class="band-red"></div>
      <div class="band-gap"></div>
      <div class="band-cyan"></div>
    </div>
  </section>

  <section class="card card-back">
    <div class="back-brand">
      <span class="brand-square"></span>
      <span class="brand-name">Corvane Supplies</span>
    </div>
    <div class="person-name">Name Surname</div>
    <div class="person-role">POSITION</div>
    <div class="divider"></div>
    <ul class="contact-list">
      <li>
        <svg viewBox="0 0 14 14"><rect x="3.5" y="0.5" width="7" height="13" rx="1.5" fill="none" stroke="#06b0d4" stroke-width="1.5"/><rect x="6" y="10.5" width="2" height="1.2" fill="#06b0d4"/></svg>
        (555) 410-2380
      </li>
      <li>
        <svg viewBox="0 0 14 14"><rect x="0.5" y="3" width="13" height="9" fill="#06b0d4"/><path d="M0.5 3 L7 8 L13.5 3" fill="none" stroke="#fff" stroke-width="1.2"/></svg>
        sales@corvanesupplies.com
      </li>
      <li>
        <svg viewBox="0 0 14 14"><circle cx="7" cy="7" r="6" fill="none" stroke="#06b0d4" stroke-width="1.3"/><ellipse cx="7" cy="7" rx="2.6" ry="6" fill="none" stroke="#06b0d4" stroke-width="1"/><path d="M1 7 H13 M2 4 H12 M2 10 H12" stroke="#06b0d4" stroke-width="1"/></svg>
        corvanesupplies.com
      </li>
    </ul>
    <div class="address">
      420 N.Harlow Suite 5<br>
      Ridgeport, Tx 79712
    </div>
  </section>
</body>
</html>
```